Kitchen and bathroom exhaust fan cleaning business card design

A new business cleaning domestic - not commercial - exhaust/extractor fans in kitchens, bathrooms and en suites and kitchen range hood filters.

We would like a bright colour suggesting cleanliness (such a syellow or light green?)

I would like to see on the card preferably on the reverse:

"We clean kitchen and bathroom exhaust fans & Volrex Brightos
and
clean and repair range hood filters and replace carbon filters

We give Pensioner discounts
Updates

Designers pls note the TM in the contact filed after Pureflow Vents should be superscript as in the trademark sign. On the reverse of the card, I would like:: "We clean kitchen and bathroom exhaust fans & Volrex Brightos & clean and repair range hood filters and replace carbon filters We give Pensioner discounts

Reason: I will be out of the country for several days

Target Market(s)

people who are too lazy or too busy to clean their fan units and pensioners and others who are unable to do it.

Industry/Entity Type

Business

Contact Information for Business Card

ACT Clean FansTM Designer pls note the TM should be superscript as in the trademark sign
Neil Oakley
Mob: 0431 572 864
Email: pureflowvents@zentromail.com
PO Box 7152, Pellow ACT 2608

Requirements
Must have
• Designer pls note the TM in the contact filed after Pureflow Vents should be superscript as in the trademark sign.

On the reverse

and

```html
<!DOCTYPE html>
<html lang="en">
<head>
<meta charset="utf-8">
<title>Pureflow Vents – Business Card</title>
<link href="https://fonts.googleapis.com/css2?family=Exo+2:wght@400;700&family=Cormorant+Garamond:wght@500&family=Open+Sans:wght@400&display=swap" rel="stylesheet">
<style>
  :root {
    --backdrop: #1c1c1c;
    --card: #000000;
    --brand-green: #1f9a4a;
    --guide-yellow: #e8e21a;
    --grille-light: #ecebe6;
    --grille-mid: #a9a8a3;
  }
  * { box-sizing: border-box; margin: 0; padding: 0; }
  html, body {
    width: 1200px; height: 900px; overflow: hidden;
    background: var(--backdrop);
  }
  .canvas { position: relative; width: 1200px; height: 900px; }

  .card {
    position: absolute; left: 300px; width: 600px; height: 343px;
    background: var(--card);
    box-shadow: 0 10px 30px rgba(0,0,0,.55);
    overflow: hidden;
  }
  .card--front { top: 70px; }
  .card--back  { top: 487px; }

  .trim-frame {
    position: absolute; inset: 18px;
    border: 1.5px solid var(--guide-yellow);
    pointer-events: none;
  }

  /* front */
  .fan-visual {
    position: absolute; left: 58px; top: 48px;
    width: 200px; height: 160px; border-radius: 50%;
    transform: rotate(-18deg);
    background: radial-gradient(ellipse at 45% 50%, var(--grille-light) 0%, #d6d5d0 60%, var(--grille-mid) 100%);
  }
  .divider {
    position: absolute; left: 300px; top: 52px;
    width: 2px; height: 180px; background: var(--guide-yellow);
  }
  .brand-block {
    position: absolute; left: 330px; top: 58px; width: 240px;
    color: var(--brand-green); text-align: center;
  }
  .brand-name {
    font-family: "Exo 2", sans-serif; font-weight: 700;
    font-size: 30px; line-height: 1;
  }
  .brand-sub {
    font-family: "Cormorant Garamond", serif; font-weight: 500;
    font-size: 19px; margin-top: 4px;
  }
  .contact-list {
    position: absolute; left: 322px; top: 150px;
    list-style: none; color: var(--brand-green);
    font-family: "Open Sans", sans-serif; font-size: 14px;
  }
  .contact-item { display: flex; align-items: center; gap: 10px; height: 23px; }
  .contact-icon { width: 14px; height: 14px; fill: var(--brand-green); flex: none; }
  sup { font-size: .55em; }

  /* back */
  .back-content {
    position: absolute; left: 40px; right: 40px; top: 70px;
    text-align: center; color: var(--brand-green);
  }
  .back-brand {
    font-family: "Exo 2", sans-serif; font-weight: 400;
    font-size: 34px; line-height: 1.1;
  }
  .back-person {
    font-family: "Exo 2", sans-serif; font-weight: 400;
    font-size: 28px; line-height: 1.15;
  }
  .service-list {
    margin: 22px auto 0; max-width: 440px;
    font-family: "Open Sans", sans-serif; font-size: 14px; line-height: 1.5;
  }
  .service-offer { margin-top: 8px; }
</style>
</head>
<body>
<main class="canvas">

  <section class="card card--front" aria-label="Card front">
    <div class="trim-frame"></div>
    <div class="fan-visual" role="img" aria-label="Photo of a white exhaust fan grille"></div>
    <div class="divider"></div>
    <div class="brand-block">
      <p class="brand-name">Pureflow</p>
      <p class="brand-sub">Vents<sup>TM</sup> Neil Oakley</p>
    </div>
    <ul class="contact-list">
      <li class="contact-item">
        <svg class="contact-icon" viewBox="0 0 14 14" aria-hidden="true"><path d="M7 0a5 5 0 0 0-5 5c0 3.6 5 9 5 9s5-5.4 5-9a5 5 0 0 0-5-5zm0 7a2 2 0 1 1 0-4 2 2 0 0 1 0 4z"/></svg>
        PO Box 7152, Pellow ACT 2608
      </li>
      <li class="contact-item">
        <svg class="contact-icon" viewBox="0 0 14 14" aria-hidden="true"><path d="M0 3h14v9H0zM1.2 4.2v.3L7 8.3l5.8-3.8v-.3z"/></svg>
        pureflowvents@zentromail.com
      </li>
      <li class="contact-item">
        <svg class="contact-icon" viewBox="0 0 14 14" aria-hidden="true"><path d="M4 0h6a1 1 0 0 1 1 1v12a1 1 0 0 1-1 1H4a1 1 0 0 1-1-1V1a1 1 0 0 1 1-1zm.5 1.5v9h5v-9zM7 11.3a.9.9 0 1 0 0 1.8.9.9 0 0 0 0-1.8z"/></svg>
        0431 572 864
      </li>
    </ul>
  </section>

  <section class="card card--back" aria-label="Card back">
    <div class="trim-frame"></div>
    <div class="back-content">
      <p class="back-brand">Pureflow Vents<sup>TM</sup></p>
      <p class="back-person">Neil Oakley</p>
      <div class="service-list">
        <p>We clean kitchen and bathroom exhaust fans &amp; Volrex Brightos &amp; clean and repair range hood filters and replace carbon filters</p>
        <p class="service-offer">We give Pensioner discounts</p>
      </div>
    </div>
  </section>

</main>
</body>
</html>
```